Letterhead

We have a new logo and would like to design electronic letterhead with our new logo. We have two office locations. One of our offices is moving in July.

```html
<!DOCTYPE html>
<html lang="en">
<head>
<meta charset="utf-8">
<title>Norwick Hale – Letterhead</title>
<link href="https://fonts.googleapis.com/css2?family=Open+Sans:wght@400;600&family=Roboto:wght@400&display=swap" rel="stylesheet">
<style>
  :root {
    --navy: #10142e;
    --blue: #1267b4;
    --text: #3a3a3a;
    --paper: #ffffff;
    --bg: #ffffff;
  }
  * { margin: 0; padding: 0; box-sizing: border-box; }
  html, body { width: 1063px; height: 1200px; overflow: hidden; background: var(--bg); }
  .letterhead {
    position: relative;
    width: 1063px;
    height: 1200px;
    background: var(--paper);
    font-family: "Open Sans", sans-serif;
    color: var(--text);
  }
  .brand {
    position: absolute;
    left: 96px;
    top: 150px;
    display: flex;
    align-items: center;
    gap: 12px;
  }
  .brand-mark { width: 14px; height: 14px; background: var(--blue); }
  .brand-name {
    font-family: "Open Sans", sans-serif;
    font-weight: 600;
    font-size: 40px;
    color: var(--navy);
    letter-spacing: 0.5px;
  }
  .contact {
    position: absolute;
    left: 716px;
    top: 70px;
    padding-left: 30px;
    border-left: 2px solid var(--navy);
    font-family: "Roboto", sans-serif;
    font-size: 15px;
    line-height: 19px;
    color: var(--navy);
  }
  .contact-line { display: flex; align-items: center; gap: 7px; }
  .contact-line svg { width: 13px; height: 13px; fill: var(--blue); flex: none; }
  .letter-body {
    position: absolute;
    left: 96px;
    top: 300px;
    width: 800px;
    font-size: 15.5px;
    line-height: 24px;
  }
  .salutation { margin-bottom: 24px; }
  .letter-body p.para { margin-bottom: 24px; }
  .closing { margin-top: 8px; }
  .signature {
    width: 150px;
    height: 80px;
    margin-top: 24px;
    background: linear-gradient(135deg, #f4f4f4, #e4e4e4);
  }
  .footer-address {
    position: absolute;
    left: 570px;
    top: 1128px;
    display: flex;
    align-items: center;
    gap: 8px;
    font-family: "Roboto", sans-serif;
    font-size: 16px;
    color: var(--navy);
  }
  .footer-address svg { width: 14px; height: 18px; fill: var(--blue); }
  .footer-band { position: absolute; left: 0; bottom: 0; width: 1063px; height: 30px; }
</style>
</head>
<body>
<main class="letterhead">
  <div class="brand">
    <span class="brand-mark"></span>
    <span class="brand-name">Norwick Hale</span>
  </div>

  <address class="contact">
    <div>118 Marlow Street 300</div>
    <div>Brookfield, WA 98010</div>
    <div class="contact-line"><svg viewBox="0 0 16 16"><path d="M2 6c0-2 2-4 6-4s6 2 6 4l-3 1-1-2H6L5 7 2 6zm2 2h8l2 6H2l2-6zm4 1.5a2 2 0 100 4 2 2 0 000-4z"/></svg>(555) 014-2270</div>
    <div class="contact-line"><svg viewBox="0 0 16 16"><path d="M4 1h8v4H4zM1 6h14v6h-3v3H4v-3H1zm4 4v4h6v-4z"/></svg>(555) 014-3381</div>
    <div class="contact-line"><svg viewBox="0 0 16 16"><path d="M1 3h14v10H1zm1.5 1.5L8 9l5.5-4.5v-.2H2.5z"/></svg>info@norwickhale.law</div>
    <div class="contact-line"><svg viewBox="0 0 16 16"><path d="M8 1a7 7 0 100 14A7 7 0 008 1zm-2 3l3 1-1 3 2 2-1 3-2-2V8L4 6z"/></svg>www.norwickhale.law</div>
  </address>

  <section class="letter-body">
    <p class="salutation">Dear customer,</p>
    <p class="para">Lorem ipsum dolor sit amet, consectetur adipisicing elit, sed do eiusmod tempor incididunt ut labore et dolore magna aliqua. Ut enim ad minim veniam, quis nostrud exercitation ullamco laboris nisi ut aliquip ex ea commodo consequat. Duis aute irure dolor in reprehenderit in voluptate velit esse cillum dolore eu fugiat nulla pariatur. Excepteur sint occaecat cupidatat non proident, sunt in culpa qui officia deserunt mollit anim id est laborum.</p>
    <p class="para">Lorem ipsum dolor sit amet, consectetur adipisicing elit, sed do eiusmod tempor incididunt ut labore et dolore magna aliqua. Ut enim ad minim veniam, quis nostrud exercitation ullamco laboris nisi ut aliquip ex ea commodo consequat. Duis aute irure dolor in reprehenderit in voluptate velit esse cillum dolore eu fugiat nulla pariatur. Excepteur sint occaecat cupidatat non proident, sunt in culpa qui officia deserunt mollit anim id est laborum.</p>
    <p class="para">Lorem ipsum dolor sit amet, consectetur adipisicing elit, sed do eiusmod tempor incididunt ut labore et dolore magna aliqua. Ut enim ad minim veniam, quis nostrud exercitation ullamco laboris nisi ut aliquip ex ea commodo consequat. Duis aute irure dolor in reprehenderit in voluptate velit esse cillum dolore eu fugiat nulla pariatur. Excepteur sint occaecat cupidatat non proident, sunt in culpa qui officia deserunt mollit anim id est laborum.</p>
    <p class="para">Lorem ipsum dolor sit amet, consectetur adipisicing elit, sed do eiusmod tempor incididunt ut labore et dolore magna aliqua. Ut enim ad minim veniam, quis nostrud exercitation ullamco laboris nisi ut aliquip ex ea commodo consequat. Duis aute irure dolor in reprehenderit.</p>
    <p class="closing">Yours Sincerely,</p>
    <div class="signature" role="img" aria-label="Handwritten signature"></div>
  </section>

  <div class="footer-address">
    <svg viewBox="0 0 14 18"><path d="M7 0a7 7 0 00-7 7c0 5 7 11 7 11s7-6 7-11a7 7 0 00-7-7zm0 4a3 3 0 110 6 3 3 0 010-6z"/></svg>
    640 Harbor Ave., Ste 200 Lakemont, WA 98400
  </div>

  <svg class="footer-band" viewBox="0 0 1063 30" preserveAspectRatio="none" aria-hidden="true">
    <polygon points="0,8 610,8 632,30 0,30" fill="var(--navy)"/>
    <polygon points="622,0 1063,0 1063,22 644,22" fill="var(--blue)"/>
  </svg>
</main>
</body>
</html>
```